Book Cover for: TITLE Mend the Quiet Hours SUBTITLE For couples who don't want to break up

We need a full cover design for a book on relationships written by husband and wife team, Marla and Walter Dunmore, PhD. This book will offer hope for couples that are on the verge of breaking up but want to work things out and stay together. The theme is to teach couples about their own reactions to their partner, how moods affect a relationship, how to get creative to solving problems and how to have a good feeling towards your partner regardless of differences. This book is about hope. It is a positive look at relationships that feel hopeless.

Target Market(s)

Married or couples that are going through a difficult time and are considering splitting up due to, communication difficulties, addiction, affair. We imagine the book will appeal to women more than men but still want a cover that men would be comfortable picking up.

Colors

Designer to choose colors to be used in the design.

Requirements
Must have
• We want the cover to beautiful, intriguing, simple and uncomplicated. We don't want it overly busy, technical, or complex.
Nice to have
• MAYBE?? a broken heart being put back together.
Should not have
• No photo, no cartoon, no flowers, no couple (unless obscure and not gender specific).

```html
<!DOCTYPE html>
<html lang="en">
<head>
<meta charset="utf-8">
<title>Mend the Quiet Hours — Full Cover</title>
<link href="https://fonts.googleapis.com/css2?family=Cormorant+Garamond:ital,wght@0,400;0,500;0,600;1,500&family=Great+Vibes&display=swap" rel="stylesheet">
<style>
  :root {
    --stage: #ecebe6;
    --paper: #f6f0cf;
    --ink: #2a2522;
    --ink-soft: #4a433d;
    --heart: #8a1d1f;
    --heart-light: #a3302f;
    --photo: #6b5b52;
    --signature: #d9cfae;
    --label: #ffffff;
  }
  * { margin: 0; padding: 0; box-sizing: border-box; }
  html, body { width: 764px; height: 1200px; overflow: hidden; background: var(--stage); }
  .canvas { position: relative; width: 764px; height: 1200px; }
  .spread {
    position: absolute; left: 0; top: 352px; width: 764px; height: 497px;
    background: var(--paper); box-shadow: 0 2px 10px rgba(0,0,0,.12);
    font-family: "Cormorant Garamond", Georgia, serif; color: var(--ink);
  }
  .back { position: absolute; left: 0; top: 0; width: 344px; height: 100%; }
  .spine { position: absolute; left: 344px; top: 0; width: 51px; height: 100%; }
  .front { position: absolute; left: 395px; top: 0; width: 369px; height: 100%; text-align: center; }

  .blurb { position: absolute; left: 22px; top: 24px; width: 300px; font-size: 11px; line-height: 1.45; font-style: italic; color: var(--ink-soft); }
  .author-photo { position: absolute; left: 22px; top: 172px; width: 112px; height: 82px; background: linear-gradient(160deg, #8a786d, var(--photo)); }
  .author-signature { position: absolute; left: 26px; top: 262px; width: 104px; height: 26px; background: var(--signature); border-radius: 3px; }
  .bio { position: absolute; left: 146px; top: 172px; width: 176px; font-size: 10.5px; line-height: 1.4; font-style: italic; color: var(--ink-soft); }
  .closing { position: absolute; left: 22px; top: 300px; width: 300px; font-size: 11px; line-height: 1.45; font-style: italic; color: var(--ink-soft); }
  .back-heart { position: absolute; left: 22px; top: 360px; width: 34px; height: 30px; border-radius: 6px; background: linear-gradient(160deg, var(--heart-light), var(--heart)); }
  .barcode-area { position: absolute; left: 22px; top: 416px; width: 92px; height: 60px; background: var(--label); }

  .spine-title, .spine-author {
    position: absolute; left: 0; width: 51px; writing-mode: vertical-rl;
    display: flex; align-items: center; justify-content: center; white-space: nowrap;
  }
  .spine-title { top: 12px; height: 210px; font-size: 17px; letter-spacing: 1px; }
  .spine-title .script { font-family: "Great Vibes", cursive; color: var(--heart); font-size: 20px; margin: 4px 0; }
  .spine-author { top: 232px; height: 200px; font-size: 12px; letter-spacing: 1.5px; font-weight: 500; line-height: 1.35; text-align: center; }
  .spine-heart { position: absolute; left: 13px; top: 450px; width: 25px; height: 22px; border-radius: 5px; background: linear-gradient(160deg, var(--heart-light), var(--heart)); }

  .tagline { position: absolute; left: 0; top: 26px; width: 100%; font-size: 15px; font-style: italic; font-weight: 500; letter-spacing: 1.5px; line-height: 1.25; }
  .title { position: absolute; left: 0; top: 72px; width: 100%; line-height: 1; }
  .title .line { display: block; font-weight: 500; letter-spacing: 2px; }
  .title .big { font-size: 54px; }
  .title .mid { font-size: 44px; }
  .title .script { display: block; font-family: "Great Vibes", cursive; color: var(--heart); font-size: 42px; margin: -10px 0 -6px; }
  .cover-heart { position: absolute; left: 92px; top: 240px; width: 185px; height: 155px; border-radius: 18px; background: linear-gradient(160deg, var(--heart-light), var(--heart)); }
  .cover-author { position: absolute; left: 0; top: 440px; width: 100%; font-size: 15px; letter-spacing: 1.5px; font-weight: 600; }
</style>
</head>
<body>
<div class="canvas">
  <section class="spread">
    <div class="back">
      <p class="blurb">Have you ever wondered how one quiet evening could undo years of closeness? Have you felt distance grow between you and the person you love most, and wondered whether anything could close it again? This book offers a gentle path back. Drawing on decades of work with couples, the authors show how moods shape what we see, and how a calmer mind opens room for warmth, patience and renewed understanding.</p>
      <div class="author-photo" role="img" aria-label="Portrait photograph of the authors"></div>
      <div class="author-signature" role="img" aria-label="Handwritten signature: Marla &amp; Walter"></div>
      <p class="bio">Marla and Walter Dunmore, Ph.D. have worked with couples for many years across workshops, retreats and private sessions. Their approach helps partners notice their own reactions and find fresh feeling for each other.</p>
      <p class="closing">They have seen how hope returns when couples stop blaming and start listening. Mend the Quiet Hours is a kind, practical guide for anyone who still believes their relationship is worth saving.</p>
      <div class="back-heart" role="img" aria-label="Small broken heart emblem"></div>
      <div class="barcode-area" aria-hidden="true"></div>
    </div>

    <div class="spine">
      <div class="spine-title"><span>MEND</span><span class="script">the</span><span>QUIET HOURS</span></div>
      <div class="spine-author">MARLA AND WALTER<br>DUNMORE, PHD</div>
      <div class="spine-heart" role="img" aria-label="Small broken heart emblem"></div>
    </div>

    <div class="front">
      <p class="tagline">FOR COUPLES WHO<br>DON’T WANT TO BREAK UP</p>
      <h1 class="title">
        <span class="line big">MEND</span>
        <span class="script">the</span>
        <span class="line mid">QUIET HOURS</span>
      </h1>
      <div class="cover-heart" role="img" aria-label="Large deep red broken heart illustration"></div>
      <p class="cover-author">MARLA AND WALTER DUNMORE, PHD</p>
    </div>
  </section>
</div>
</body>
</html>
```